Postcard Design -- Brookfern Collective

Brookfern Collective believes that when low-income immigrants acquire the right tools (skills and abilities), they can overcome poverty and build a pathway to success as new Americans. We accomplish this through our wraparound strategy, which offers a full range of services designed to help people overcome barriers to the acquisition of the skills and abilities they need to thrive. This process involves recognizing the diverse skills immigrants already possess, resolving immediate needs or problems, identifying opportunities for growth, and monitoring progress toward goals. As a result, clients are able to acquire the skills and abilities they need to thrive as new Americans.

We need a postcard design that follows the Brookfern Collective brand, but also has a heartwarming/holiday feel to it with a cool factor. This postcard will be mailed as an insert with our appeal letter. The purpose of this postcard is to encourage donors who receive it to reuse/mail it to someone else and encourage them to donate to Brookfern Collective.

Target Market(s)

Donors

Industry/Entity Type

Non-Profit

Font styles to use
Sans Serif

Requirements
Must have
• Our Colors: #3276b5 #9bcb3c #fece3e #f04a50
• Double sided Postcard:
• Front side:
• - A design that is welcoming and has a heartwarming/holiday feel to it
• - Our logo
• - and a message (examples: 'Thinking About You'.. 'Giving back to the community'.. 'Celebrate with us'.. 'Sharing the holiday spirit'.. 'Share the cheer'.. 'Invest in our community'..) I'm open to new ideas.
• Back side:
• - Mission Statement
• - We help low-income, Spanish-speaking immigrants acquire the tools they need to thrive.
• - Logo
• - site link (brookferncollective.org)
• - donation link (donate.brookferncollective.org)
• - Call to action (Invest in Brookfern Collective Today!.. Wishing you Happy Holidays, join me in supporting New-Americans today.. etc)
• - Leave area available for sender info and person receiving info (like a regular postcard)
• - 4155550187
• -FB and Twitter icon
Nice to have
• Postcard Final Dimension: 3.5"x5" (with bleed, PLEASE)
• PROJECT SPECIFICS
• Audience = Donors
• Message = Asking other to invest on Brookfern Collective
• Product = Postcard Design 3.5"x5"
• Font = Sans Serif

```html
<!DOCTYPE html>
<html lang="en">
<head>
<meta charset="utf-8">
<title>Brookfern Collective Holiday Postcard</title>
<link rel="stylesheet" href="https://fonts.googleapis.com/css2?family=Raleway:ital,wght@0,400;0,700;1,400;1,700&family=Niconne&family=Cinzel:wght@500&display=swap">
<style>
  :root {
    --brand-blue: #3276b5;
    --deep-blue: #1a6fa8;
    --brand-green: #9bcb3c;
    --leaf-green: #6aa83a;
    --brand-yellow: #fece3e;
    --brand-red: #f04a50;
    --wine-red: #a51c2a;
    --paper: #ffffff;
    --frost: #ececec;
  }
  * { margin: 0; padding: 0; box-sizing: border-box; }
  html, body { width: 1200px; height: 1200px; overflow: hidden; background: var(--paper); }
  .canvas { position: relative; width: 1200px; height: 1200px; font-family: "Raleway", sans-serif; }

  /* Front side grid */
  .front { position: absolute; left: 194px; top: 42px; width: 782px; height: 548px;
    display: grid; grid-template-columns: 264px 262px 256px; grid-template-rows: 276px 272px; }
  .tile { position: relative; overflow: hidden; }
  .message { display: flex; align-items: center; justify-content: center; text-align: center;
    font-family: "Niconne", cursive; color: var(--paper); line-height: 0.92;
    text-shadow: 0 2px 6px rgba(0,0,0,0.25); }
  .message--green {
    background:
      radial-gradient(circle at 50% 42%, rgba(255,255,255,0.28), rgba(255,255,255,0) 55%),
      radial-gradient(circle at 50% 50%, #a9d23c, #7db42a 80%);
    font-size: 60px; }
  .message--blue {
    background:
      radial-gradient(circle at 50% 45%, rgba(120,190,240,0.35), rgba(120,190,240,0) 60%),
      radial-gradient(circle at 50% 50%, #2a7fbf, #135f9c 85%);
    font-size: 56px; }
  .photo--snow {
    background:
      radial-gradient(ellipse 34% 48% at 50% 62%, #ffffff 0%, #f2f4f7 60%, rgba(242,244,247,0) 100%),
      radial-gradient(ellipse 22% 30% at 18% 38%, rgba(40,70,150,0.75), rgba(40,70,150,0) 100%),
      radial-gradient(ellipse 20% 30% at 82% 40%, rgba(120,180,220,0.6), rgba(120,180,220,0) 100%),
      radial-gradient(ellipse 25% 14% at 52% 70%, rgba(110,70,160,0.55), rgba(110,70,160,0) 100%),
      linear-gradient(180deg, #6e5a45 0%, #9a8a76 30%, #dfe4ea 70%, #f6f7f9 100%); }
  .photo--garden {
    background:
      radial-gradient(ellipse 35% 30% at 52% 35%, rgba(235,185,150,0.9), rgba(235,185,150,0) 100%),
      radial-gradient(ellipse 30% 35% at 22% 80%, rgba(214,50,110,0.85), rgba(214,50,110,0) 100%),
      radial-gradient(ellipse 28% 30% at 85% 85%, rgba(240,150,190,0.8), rgba(240,150,190,0) 100%),
      linear-gradient(160deg, #6d8a3e 0%, #b9c46a 35%, #e9c9a0 60%, #d98aa8 100%); }
  .photo--family {
    background:
      radial-gradient(ellipse 30% 35% at 25% 45%, rgba(245,125,100,0.9), rgba(245,125,100,0) 100%),
      radial-gradient(ellipse 30% 30% at 62% 55%, rgba(170,200,235,0.9), rgba(170,200,235,0) 100%),
      radial-gradient(ellipse 22% 22% at 85% 30%, rgba(120,185,110,0.8), rgba(120,185,110,0) 100%),
      linear-gradient(165deg, #5c7f63 0%, #8aa7b0 35%, #d9b79c 65%, #6f8fb8 100%); }
  .brand-tile {
    background:
      radial-gradient(ellipse 60% 40% at 50% 60%, #ffffff 40%, rgba(255,255,255,0) 100%),
      linear-gradient(180deg, #bdbdbd 0%, #e4e4e4 35%, #ffffff 75%);
    display: flex; flex-direction: column; align-items: center; justify-content: center; gap: 14px; padding-top: 10px; }
  .brand-mark { width: 128px; height: 128px; background: var(--brand-blue); }
  .brand-name { font-weight: 700; color: var(--brand-blue); font-size: 34px; text-align: center; line-height: 1.0; }

  /* Back side */
  .back-band { position: absolute; left: 194px; top: 612px; width: 782px; height: 208px;
    background:
      radial-gradient(ellipse 30% 60% at 82% 40%, rgba(255,255,255,0.9), rgba(255,255,255,0) 100%),
      linear-gradient(180deg, var(--frost) 0%, #f6f6f6 65%, var(--paper) 100%); }
  .back-copy { position: absolute; left: 210px; top: 620px; width: 382px; text-align: center; }
  .mission { font-size: 22px; line-height: 23px; color: var(--wine-red); letter-spacing: -0.4px; }
  .mission strong { font-style: italic; font-weight: 700; }
  .back-brand { margin-top: 14px; display: flex; align-items: center; justify-content: center; gap: 8px; }
  .back-brand .brand-mark { width: 58px; height: 58px; }
  .back-brand .brand-name { font-size: 25px; }
  .site { font-size: 26px; color: var(--leaf-green); margin-top: 6px; line-height: 30px; }
  .donate { font-size: 26px; color: var(--deep-blue); line-height: 30px; }
  .rule { width: 304px; height: 6px; background: var(--brand-yellow); margin: 6px auto 0; }
  .invest { font-family: "Cinzel", serif; font-size: 21px; color: var(--leaf-green); line-height: 23px; margin-top: 10px; }
  .wish { font-family: "Niconne", cursive; font-size: 34px; color: var(--wine-red); line-height: 34px; margin-top: 6px; }
  .phone { font-size: 25px; color: var(--deep-blue); margin: 4px 0 6px; }
  .social { display: flex; justify-content: center; gap: 22px; margin-top: 14px; }
  .social span { width: 46px; height: 46px; border-radius: 50%; background: var(--deep-blue); display: block; }
  .social span + span { background: #3aa0d8; }
</style>
</head>
<body>
<div class="canvas">
  <section class="front">
    <div class="tile message message--green" role="img" aria-label="Green panel with falling snow dots">Sharing<br>the<br>holiday<br>spirit</div>
    <div class="tile photo--snow" role="img" aria-label="Photo of a smiling couple hugging a snowman in a purple scarf, winter forest behind"></div>
    <div class="tile message message--blue" role="img" aria-label="Blue panel with snowflake pattern">Giving<br>back<br>to the<br>Community</div>
    <div class="tile photo--garden" role="img" aria-label="Photo of a mother with two young daughters in a sunny garden"></div>
    <div class="tile brand-tile" role="img" aria-label="Silver panel with white snowflakes behind the brand name">
      <span class="brand-mark"></span>
      <span class="brand-name">Brookfern<br>Collective</span>
    </div>
    <div class="tile photo--family" role="img" aria-label="Photo of a smiling family of four sitting together by a lake"></div>
  </section>

  <div class="back-band" role="img" aria-label="Soft white snowflake background"></div>
  <section class="back-copy">
    <p class="mission"><strong>We help</strong> low-income,<br><strong>Spanish-speaking immigrants</strong><br>acquire the <strong>tools they need to thrive.</strong></p>
    <div class="back-brand">
      <span class="brand-mark"></span>
      <span class="brand-name">Brookfern Collective</span>
    </div>
    <p class="site">brookferncollective.org</p>
    <p class="donate">donate.brookferncollective.org</p>
    <div class="rule"></div>
    <p class="invest">Invest in<br>Brookfern Collective Today!..</p>
    <p class="wish">Wishing you<br>Happy Holidays,<br>join me in supporting<br>New-Americans today..</p>
    <div class="rule"></div>
    <p class="phone">415.555.0187</p>
    <div class="rule" style="margin-top:0"></div>
    <div class="social" aria-label="Social media links">
      <span></span><span></span>
    </div>
  </section>
</div>
</body>
</html>
```